Private practice for psychiatry and psychotherapy needs a business card and logo

I need a logo and business card design for my private practice for psychiatry and psychotherapy. The optional names for my practice are: Vornhoute Praktijk voor Psychiatrie en Psychotherapie, or short: Praktijk Vornhoute.
I am a (child and adolescent) psychiatrist and psychotherapist. I diagnose and treat infants, children, adolescents and adults with psychiatric symptoms/disorders. I also give supervision to colleagues about their own treatments. My work is characterised by personal involvement, transparence, creativity and professionality.
I would like to have an appealing, light and bright, yet basic design that invites people (both children and adults) to contact me, gives trust and hope, without loosing professional appearance.
I uploaded my contact information which should not necessarily be all included (in this form) on the card as long as people know how to contact me. Please feel free to be creative!
Please note that my website is only temporarely and need a new design and update too!

Target Market(s)

Clients and patients (children, adolescents, adults) with psychiatric symptoms who need diagnosis and treatment. I work with private clients and patients through medical insurances.

Industry/Entity Type

Mental Health

Contact Information for Business Card

Dr. Sanne Vornhoute-ter Kuilen
Psychiater/Kinder- en Jeugdpsychiater
Wouter Heskampstraat 14
3071 PX Rotterdam
t: 06-51928764
e: info@praktijkvornhoute.nl
i: www.praktijkvornhoute.nl

Logo Text

Praktijk Vornhoute voor Psychiatrie en Psychotherapie; or short: Praktijk Vornhoute

Font styles to use
Sans Serif
Other font styles liked:
• up to designer

Requirements
Must have
• Appealing, light, bright, creative, trustful, professional and unique.

```html
<!DOCTYPE html>
<html lang="nl">
<head>
<meta charset="utf-8">
<title>Praktijk Vornhoute – visitekaartje</title>
<link href="https://fonts.googleapis.com/css2?family=Oswald:wght@400;500&display=swap" rel="stylesheet">
<style>
  :root {
    --navy: #0d4f86;
    --navy-deep: #0a3f6e;
    --sky: #1ab0e6;
    --olive: #b5a82c;
    --paper: #ffffff;
    --backdrop: #eef1f4;
  }
  * { margin: 0; padding: 0; box-sizing: border-box; }
  html, body { width: 1200px; height: 960px; overflow: hidden; }
  body {
    background: var(--backdrop);
    font-family: "Oswald", "Arial Narrow", sans-serif;
    position: relative;
  }
  .card {
    position: absolute;
    left: 232px;
    width: 736px;
    height: 420px;
    background: var(--paper);
    box-shadow: 0 6px 18px rgba(0,0,0,.12);
    overflow: hidden;
  }
  .card--front { top: 40px; }
  .card--back { top: 500px; }
  .card svg.deco { position: absolute; inset: 0; }

  .wordmark {
    position: absolute;
    display: flex;
    align-items: center;
    gap: 14px;
    font-weight: 500;
    color: var(--sky);
    white-space: nowrap;
  }
  .wordmark__dot {
    border-radius: 50%;
    background: var(--sky);
    flex: none;
  }
  .card--front .wordmark { left: 0; right: 0; justify-content: center; top: 120px; font-size: 56px; }
  .card--front .wordmark__dot { width: 40px; height: 40px; }
  .website {
    position: absolute; left: 0; right: 0; top: 258px;
    text-align: center; color: var(--navy); font-size: 34px; font-weight: 500;
  }

  .card--back .wordmark { left: 28px; top: 236px; font-size: 30px; }
  .card--back .wordmark__dot { width: 22px; height: 22px; }

  .details { position: absolute; right: 48px; top: 56px; text-align: right; }
  .details__name { color: var(--navy); font-size: 26px; font-weight: 500; line-height: 1.15; white-space: nowrap; }
  .details__rule { height: 3px; background: var(--sky); margin: 8px 0 6px auto; width: 330px; }
  .details__role { color: var(--olive); font-size: 17px; }
  .contact { margin-top: 40px; color: var(--navy); font-size: 20px; line-height: 1.55; }
  .contact__label { color: var(--olive); }
</style>
</head>
<body>

<section class="card card--front" aria-label="Voorkant visitekaartje">
  <svg class="deco" width="736" height="420" viewBox="0 0 736 420" aria-hidden="true">
    <path d="M0 80 H70 V112 H28 V150 H0 Z" fill="var(--olive)"/>
    <rect x="0" y="150" width="28" height="50" fill="var(--sky)"/>
    <rect x="0" y="200" width="28" height="56" fill="var(--navy)"/>
  </svg>
  <div class="wordmark"><span class="wordmark__dot"></span>Praktijk Vornhoute</div>
  <p class="website">www.praktijkvornhoute.nl</p>
</section>

<section class="card card--back" aria-label="Achterkant visitekaartje">
  <svg class="deco" width="736" height="420" viewBox="0 0 736 420" aria-hidden="true">
    <path d="M0 0 H200 C300 100 340 260 310 420 H0 Z" fill="var(--navy)"/>
    <path d="M0 0 H170 C265 100 300 260 272 420 H0 Z" fill="var(--navy-deep)" opacity=".35"/>
    <path d="M236 0 C336 100 376 260 346 420" fill="none" stroke="var(--sky)" stroke-width="6"/>
    <path d="M666 0 H736 V74 H704 V32 H666 Z" fill="var(--olive)"/>
    <rect x="708" y="74" width="28" height="46" fill="var(--sky)"/>
    <rect x="708" y="120" width="28" height="52" fill="var(--navy)"/>
  </svg>
  <div class="wordmark"><span class="wordmark__dot"></span>Praktijk Vornhoute</div>
  <div class="details">
    <p class="details__name">Dr. Sanne Vornhoute-ter Kuilen</p>
    <div class="details__rule"></div>
    <p class="details__role">Psychiater/kinder- en jeugdpsychiater</p>
    <div class="contact">
      <p>Wouter Heskampstraat 14</p>
      <p>3071 PX Rotterdam</p>
      <p><span class="contact__label">t:</span> 06-51928764</p>
      <p><span class="contact__label">e:</span> info@praktijkvornhoute.nl</p>
    </div>
  </div>
</section>

</body>
</html>
```